pharmacy postcard advertiser for our new service called PerkMeds

Target Market(s)

general public. home mailer

Font styles to use
Serif

Requirements
Must have
• Double sided in color:
• Front side to contain: Picture of PerkMeds card with tagline
• Image of prescription bottle, maybe tilted with a few tabs coming out
• Big Print Tagline: Up to 5 Free Rxs Prescriptions
• for Transferred Prescriptions*
• wording on front:
• yes, its free
• yes, you will save
• yes, its easy to sign up
• Note: This is an advertiser mailer, need to leave room on left side of mailer for address. My preference for address is upper right side of card.
• Note: I will send a sketch drawing of flyer.
• Note: need a call to action (Example: Call today to start your PerkMeds benefits
Nice to have

```html
<!DOCTYPE html>
<html lang="en">
<head>
<meta charset="utf-8">
<title>PerkMeds Postcard Mailer</title>
<link rel="stylesheet" href="https://fonts.googleapis.com/css2?family=Montserrat:wght@500;700;800&family=Mulish:wght@400;600;700&display=swap">
<style>
  :root {
    --stage: #1f1f1f;
    --paper: #ffffff;
    --paper-soft: #f2f3f5;
    --brand-blue: #1b5ea9;
    --brand-red: #d11f31;
    --brand-red-dark: #9d1422;
    --ink: #2a2b2e;
    --ink-grey: #6a6c70;
    --navy: #17263a;
    --pill: #e9eaec;
    --line: #b9bcc0;
    --arc-grey: #c9cbcf;
  }
  * { box-sizing: border-box; margin: 0; padding: 0; }
  html, body { width: 900px; height: 1200px; overflow: hidden; }
  body { background: var(--stage); position: relative; font-family: "Mulish", sans-serif; color: var(--ink); }

  .card { position: absolute; left: 55px; width: 795px; background: var(--paper); overflow: hidden; }
  .card--front { top: 62px; height: 510px; }
  .card--back { top: 612px; height: 512px; }
  .card svg.shapes { position: absolute; inset: 0; }

  .headline { position: absolute; left: 33px; top: 24px; font-family: "Montserrat", sans-serif; }
  .headline__offer { font-size: 45px; font-weight: 800; line-height: 46px; color: var(--brand-blue); }
  .headline__offer span { color: var(--brand-red); }
  .headline__item { font-size: 31px; font-weight: 800; line-height: 38px; color: var(--ink-grey); }
  .headline__note { font-family: "Mulish", sans-serif; font-size: 22px; line-height: 28px; color: var(--ink); }

  .pill { position: absolute; height: 36px; border-radius: 18px; background: linear-gradient(#fafafa, var(--pill)); box-shadow: 0 2px 3px rgba(0,0,0,.18); display: flex; align-items: center; font-size: 18px; color: var(--ink); white-space: nowrap; }
  .pill__dot { width: 26px; height: 26px; border-radius: 50%; background: var(--paper); border: 3px solid var(--brand-blue); margin: 0 10px 0 5px; flex: none; }
  .pill--bold { font-weight: 700; font-size: 15px; }

  .cta-label { position: absolute; color: var(--paper); font-weight: 700; font-size: 14.5px; white-space: nowrap; }
  .card--back .cta-label { color: var(--ink); font-size: 13px; }
  .phone-badge { position: absolute; border-radius: 8px; background: linear-gradient(var(--brand-red), var(--brand-red-dark)); box-shadow: 0 3px 6px rgba(0,0,0,.35); display: flex; align-items: center; justify-content: center; gap: 8px; color: var(--paper); font-size: 38px; font-weight: 400; white-space: nowrap; }
  .phone-badge svg { width: 28px; height: 28px; flex: none; }

  .address { position: absolute; display: flex; gap: 10px; font-size: 12.5px; line-height: 16px; }
  .address svg { width: 14px; height: 20px; flex: none; margin-top: 2px; }
  .card--front .address { color: var(--paper); }

  .brand { position: absolute; }
  .brand__row { display: flex; align-items: center; gap: 10px; }
  .brand__square { background: var(--brand-blue); flex: none; }
  .brand__name { font-weight: 600; color: var(--ink-grey); }
  .brand__tagline { color: var(--brand-blue); font-weight: 600; }

  .product-visual { position: absolute; left: 395px; top: 196px; width: 400px; height: 294px; background: radial-gradient(ellipse at 40% 50%, #ffffff 0%, #e8eef2 45%, #b9d3de 100%); border-radius: 6px; }

  .copy { position: absolute; font-size: 9.2px; line-height: 12.6px; color: var(--ink); }
  .stamp { position: absolute; left: 695px; top: 34px; width: 66px; height: 70px; background: #e5e6e8; }
  .address-line { position: absolute; left: 462px; width: 280px; height: 1px; background: var(--line); }
</style>
</head>
<body>

<section class="card card--front">
  <svg class="shapes" viewBox="0 0 795 510" aria-hidden="true">
    <path d="M395 0 Q430 180 795 210 L795 238 Q410 205 372 0 Z" fill="var(--arc-grey)"/>
    <path d="M405 0 Q445 170 795 196 L795 222 Q425 190 392 0 Z" fill="var(--brand-red)"/>
    <path d="M0 345 Q320 300 795 430 L795 510 L0 510 Z" fill="var(--navy)"/>
    <path d="M0 340 Q320 295 795 424" fill="none" stroke="var(--brand-red)" stroke-width="8"/>
    <path d="M0 355 Q320 312 795 440" fill="none" stroke="var(--arc-grey)" stroke-width="2"/>
  </svg>

  <div class="headline">
    <p class="headline__offer">UP TO <span>5 FREE</span></p>
    <p class="headline__item">RXS PRESCRIPTIONS</p>
    <p class="headline__note">for Transferred Prescriptions*</p>
  </div>

  <div class="pill" style="left:33px;top:155px;width:193px"><span class="pill__dot"></span>yes, its free</div>
  <div class="pill" style="left:33px;top:205px;width:218px"><span class="pill__dot"></span>yes, you will save</div>
  <div class="pill" style="left:33px;top:255px;width:264px"><span class="pill__dot"></span>yes, its easy to sign up</div>

  <div class="brand" style="left:497px;top:30px">
    <div class="brand__row">
      <span class="brand__square" style="width:44px;height:44px"></span>
      <span class="brand__name" style="font-size:38px">PerkMeds</span>
    </div>
    <p class="brand__tagline" style="font-size:14px;line-height:15px;margin-left:88px">The Best Pharmacy<br>Savings in the USA</p>
  </div>

  <div class="product-visual" role="img" aria-label="Photo of two white prescription bottles with coloured labels"></div>

  <p class="cta-label" style="left:44px;top:360px">Call today to start your PerkMeds benefits</p>
  <div class="phone-badge" style="left:35px;top:385px;width:318px;height:55px">
    <svg viewBox="0 0 24 24"><path fill="#fff" d="M6.6 10.8a15.1 15.1 0 0 0 6.6 6.6l2.2-2.2c.3-.3.7-.4 1-.2 1.1.4 2.3.6 3.6.6.6 0 1 .4 1 1V20c0 .6-.4 1-1 1A17 17 0 0 1 3 4c0-.6.4-1 1-1h3.5c.6 0 1 .4 1 1 0 1.3.2 2.5.6 3.6.1.3 0 .7-.2 1z"/></svg>
    555-014-2290
  </div>
  <div class="address" style="left:52px;top:450px">
    <svg viewBox="0 0 14 20"><path fill="var(--brand-red)" d="M7 0a7 7 0 0 0-7 7c0 5 7 13 7 13s7-8 7-13a7 7 0 0 0-7-7zm0 9.5A2.5 2.5 0 1 1 7 4.5a2.5 2.5 0 0 1 0 5z"/></svg>
    <p>Lakeside Pharmacy, 4120 Maple Ridge Rd., Suite 20<br>Cedar Hollow, TX 75001</p>
  </div>
</section>

<section class="card card--back">
  <svg class="shapes" viewBox="0 0 795 512" aria-hidden="true">
    <path d="M0 0 L296 0 Q496 256 302 512 L0 512 Z" fill="var(--paper-soft)"/>
    <path d="M298 0 Q498 256 304 512" fill="none" stroke="var(--arc-grey)" stroke-width="16"/>
    <path d="M307 0 Q507 256 313 512" fill="none" stroke="var(--brand-red)" stroke-width="10"/>
  </svg>

  <div class="pill pill--bold" style="left:34px;top:28px;width:192px"><span class="pill__dot"></span>What is PerkMeds?</div>
  <p class="copy" style="left:34px;top:76px;width:298px">MAXIMIZE YOUR SAVINGS – PerkMeds is a prescription savings service designed to save on both insured and uninsured prescriptions. By using Lakeside Pharmacy as your primary pharmacy, PerkMeds is able to sort and find to best possible savings on your prescription medications. We are very confident that PerkMeds will produce significant savings for most pharmacy customers. No other pharmacy discount program can match the coverage offered by PerkMeds.</p>

  <div class="pill pill--bold" style="left:34px;top:182px;width:192px"><span class="pill__dot"></span>How do I sign up?*</div>
  <p class="copy" style="left:34px;top:232px;width:290px">Complete form and submit to or bring to:<br>Lakeside Pharmacy<br>Phone: 555-014-2290<br>Fax: 555-014-2291<br>4120 Maple Ridge Rd., Suite 20<br>Cedar Hollow, TX 75001</p>

  <p class="cta-label" style="left:42px;top:330px">Call today to start your PerkMeds benefits</p>
  <div class="phone-badge" style="left:34px;top:352px;width:287px;height:52px;font-size:34px">
    <svg viewBox="0 0 24 24"><path fill="#fff" d="M6.6 10.8a15.1 15.1 0 0 0 6.6 6.6l2.2-2.2c.3-.3.7-.4 1-.2 1.1.4 2.3.6 3.6.6.6 0 1 .4 1 1V20c0 .6-.4 1-1 1A17 17 0 0 1 3 4c0-.6.4-1 1-1h3.5c.6 0 1 .4 1 1 0 1.3.2 2.5.6 3.6.1.3 0 .7-.2 1z"/></svg>
    555-014-2290
  </div>

  <div class="brand" style="left:82px;top:416px">
    <div class="brand__row">
      <span class="brand__square" style="width:36px;height:36px"></span>
      <span class="brand__name" style="font-size:30px">PerkMeds</span>
    </div>
    <p class="brand__tagline" style="font-size:11px;line-height:12px;margin-left:64px">The Best Pharmacy<br>Savings in the USA</p>
  </div>

  <div class="address" style="left:378px;top:54px">
    <svg viewBox="0 0 14 20"><path fill="var(--brand-red)" d="M7 0a7 7 0 0 0-7 7c0 5 7 13 7 13s7-8 7-13a7 7 0 0 0-7-7zm0 9.5A2.5 2.5 0 1 1 7 4.5a2.5 2.5 0 0 1 0 5z"/></svg>
    <p>Lakeside Pharmacy, 4120 Maple Ridge Rd.,<br>Suite 20 Cedar Hollow, TX 75001</p>
  </div>

  <div class="stamp"></div>
  <div class="address-line" style="top:208px"></div>
  <div class="address-line" style="top:250px"></div>
  <div class="address-line" style="top:293px"></div>
</section>

</body>
</html>
```